An anniversary gift for my girlfriend

My girlfriend and I have been dating for almost 2 years. We met online and this has afforded us the really unique opportunity to have the first words we said to each other (the whole conversation, in fact) preserved. We're moving in together in a few months and she doesn't know that I saved the conversation. I've been waiting for this to turn it into something we can hang in our new place.

The only phrase I want to use is:
"Well if you dislike people's knees then I think we'll get along famously"

It's an Nobody Sleeps on Marlow Street reference for the curious.

I want the poster to use the words themselves as the art; I'm thinking typography. I'd like it to match her aesthetic, she likes to wear Lena Vireo and T. Dorn. Colors shouldn't be anything too "girly". Somewhere I'd like to include the date June 1, 2015. It shouldn't be a major piece of the poster though, just a way to denote the date.

It should fit (and be fully visible in) a 16x20 (inches) frame

Thanks in advance for the work!

Font styles to use
Serif
Decorative
Script

Requirements
Must have
• Must use only the words: "Well if you dislike people's knees then I think we'll get along famously"
• I want this to be typography, so making the phrase the center of the poster and the art itself.

```html
<!DOCTYPE html>
<html lang="en">
<head>
<meta charset="utf-8">
<title>Famously — Anniversary Poster</title>
<link rel="stylesheet" href="https://fonts.googleapis.com/css2?family=Zilla+Slab:wght@300&family=Courier+Prime:wght@700&display=swap">
<style>
  :root {
    --backdrop: #ececea;
    --poster-orange: #ea6c0c;
    --photo-light: #f6a431;
    --photo-mid: #ef8a1c;
    --ink-light: #fff6ec;
    --ink-dark: #3a1a05;
  }
  * { margin: 0; padding: 0; box-sizing: border-box; }
  html, body {
    width: 1200px;
    height: 1148px;
    overflow: hidden;
    background: var(--backdrop);
  }
  .poster {
    position: absolute;
    left: 160px;
    top: 24px;
    width: 880px;
    height: 1100px;
    background: var(--poster-orange);
    overflow: hidden;
  }
  .poster__photo {
    position: absolute;
    left: 0;
    top: 0;
    width: 500px;
    height: 100%;
    background: linear-gradient(90deg, var(--photo-light) 0%, var(--photo-mid) 70%, rgba(234,108,12,0) 100%);
  }
  .poster__phrase {
    position: absolute;
    left: 530px;
    top: 118px;
    font-family: "Zilla Slab", Georgia, serif;
    font-weight: 300;
    font-size: 52px;
    line-height: 66px;
    color: var(--ink-light);
    text-transform: uppercase;
    list-style: none;
    letter-spacing: 0.01em;
  }
  .poster__date {
    position: absolute;
    left: 540px;
    top: 925px;
    font-family: "Courier Prime", "Courier New", monospace;
    font-weight: 700;
    font-size: 17px;
    color: var(--ink-dark);
    letter-spacing: 0.02em;
  }
</style>
</head>
<body>
  <main class="poster">
    <div class="poster__photo" role="img" aria-label="Warm orange-toned photo of a woman in a patterned skirt with a vintage camera hanging on a leather strap"></div>
    <ul class="poster__phrase">
      <li>Well</li>
      <li>If</li>
      <li>You</li>
      <li>Dislike</li>
      <li>People's</li>
      <li>Knees</li>
      <li>Then</li>
      <li>I think</li>
      <li>We'll</li>
      <li>Get</li>
      <li>Along</li>
      <li>Famously</li>
    </ul>
    <p class="poster__date">JUNE 1, 2015</p>
  </main>
</body>
</html>
```